Bref créative
BRN Tek
B-cards, letter head and envelopes
I need single sided standard sized Business Card [3.5" x 2"]
use same font or others...other fonts are welcome
Simple
Gareth Pembly
CEO
482 Harlowe Street, Suite 1730
San Francisco, California 94111
gpembly@brnqel.com
brnqel.com
-use this logo in the business cards, letterhead and envelopes.
-we are looking for designs with and with out a water mark using parts or the entire logo.

```html
<!DOCTYPE html>
<html lang="en">
<head>
<meta charset="utf-8">
<title>BRN Tek Stationery</title>
<link href="https://fonts.googleapis.com/css2?family=Open+Sans:wght@400;600;800&display=swap" rel="stylesheet">
<style>
:root{
  --green:#8dc63f;
  --blue:#2d5b8c;
  --paper:#ffffff;
  --edge:#d9d9d9;
  --ink:#555555;
}
*{margin:0;padding:0;box-sizing:border-box}
html,body{width:1200px;height:797px;overflow:hidden;background:#fff}
body{position:relative;font-family:"Open Sans",Arial,sans-serif}
.sheet{position:absolute;background:var(--paper);border:1px solid var(--edge);overflow:hidden;box-shadow:0 1px 3px rgba(0,0,0,.12)}
.corner{position:absolute;top:0;right:0}
.corner.bottom{top:auto;bottom:0}
.brand{position:absolute;display:flex;align-items:center;gap:8px}
.brand .dot{border-radius:50%;background:var(--green)}
.brand .name{font-weight:800;color:var(--blue);letter-spacing:1px;line-height:1}
.letterhead{left:48px;top:19px;width:557px;height:740px}
.letterhead .brand{left:26px;top:40px}
.letterhead .dot{width:22px;height:22px}
.letterhead .name{font-size:54px}
.letterhead .footer{position:absolute;left:24px;bottom:22px;font-size:9px;color:var(--green);line-height:1.6}
.flap{position:absolute;left:173px;top:247px;width:523px;height:108px;background:var(--green);border-radius:24px 26px 0 0;overflow:hidden}
.flap .tip{position:absolute;right:0;top:0;width:86px;height:108px;background:var(--blue)}
.flap .brand{left:205px;top:30px}
.flap .dot{width:16px;height:16px}
.flap .name{font-size:44px;color:var(--blue)}
.envelope{left:48px;top:355px;width:648px;height:317px}
.envelope .brand{left:26px;top:34px}
.envelope .dot{width:20px;height:20px}
.envelope .name{font-size:50px}
.envelope .address{position:absolute;left:26px;top:232px;font-size:10px;color:var(--green);line-height:1.5}
.card{width:226px;height:133px}
.card.one{left:701px;top:343px}
.card.two{left:944px;top:343px;background:var(--blue);border-color:var(--blue)}
.card.three{left:701px;top:492px}
.card.four{left:944px;top:492px;background:var(--green);border-color:var(--green)}
.card .brand.small{left:10px;top:12px;gap:5px}
.card .brand.small .dot{width:9px;height:9px}
.card .brand.small .name{font-size:24px}
.card .person{position:absolute;font-size:10px;color:var(--green);font-weight:600}
.card .person span{display:block;font-size:6px;color:var(--ink);font-weight:400}
.card .details{position:absolute;font-size:5.5px;color:var(--ink);line-height:1.5}
.card.one .person{left:12px;top:76px}
.card.one .details{left:92px;top:16px}
.card.three .person{left:120px;top:16px}
.card.three .details{left:12px;top:66px}
.card.three .brand.small{top:20px}
.card .brand.large{left:40px;top:38px;gap:10px}
.card .brand.large .dot{width:16px;height:16px}
.card .brand.large .name{font-size:46px}
.card.two .brand.large .name{color:var(--green)}
.card.two .brand.large .dot{background:#fff}
.card.four .brand.large .dot{background:#fff}
</style>
</head>
<body>

<section class="sheet letterhead">
  <svg class="corner" width="170" height="170" viewBox="0 0 170 170">
    <circle cx="188" cy="-24" r="176" fill="var(--blue)"/>
    <circle cx="200" cy="-34" r="170" fill="var(--green)"/>
  </svg>
  <div class="brand"><span class="dot"></span><span class="name">BRN</span></div>
  <div class="footer">
    482 Harlowe Street, Suite 1730, San Francisco, California 94111<br>
    Toll free: 800-555-0142 | Phone: 414-555-0187 | Cell: 415-555-0163 | Fax: 415-555-0129 | www.brnqel.com
  </div>
</section>

<div class="flap">
  <div class="tip"></div>
  <div class="brand"><span class="name">BRN</span><span class="dot"></span></div>
</div>

<section class="sheet envelope">
  <svg class="corner" width="150" height="150" viewBox="0 0 150 150">
    <circle cx="168" cy="-20" r="156" fill="var(--blue)"/>
    <circle cx="180" cy="-30" r="150" fill="var(--green)"/>
  </svg>
  <div class="brand"><span class="dot"></span><span class="name">BRN</span></div>
  <div class="address">482 Harlowe Street, Suite 1730<br>San Francisco, California 94111</div>
</section>

<section class="sheet card one">
  <svg class="corner" width="70" height="70" viewBox="0 0 70 70">
    <circle cx="76" cy="-8" r="66" fill="var(--blue)"/>
    <circle cx="82" cy="-12" r="63" fill="var(--green)"/>
  </svg>
  <div class="brand small"><span class="dot"></span><span class="name">BRN</span></div>
  <div class="details">482 Harlowe Street, Suite 1730<br>San Francisco, California 94111<br>Phone: 414-555-0187<br>Cell: 415-555-0163<br>Fax: 415-555-0129<br>gpembly@brnqel.com<br>brnqel.com</div>
  <div class="person">Gareth Pembly<span>CEO</span></div>
</section>

<section class="sheet card two">
  <div class="brand large"><span class="dot"></span><span class="name">BRN</span></div>
</section>

<section class="sheet card three">
  <svg class="corner bottom" width="70" height="70" viewBox="0 0 70 70">
    <circle cx="76" cy="78" r="66" fill="var(--blue)"/>
    <circle cx="82" cy="82" r="63" fill="var(--green)"/>
  </svg>
  <div class="brand small"><span class="dot"></span><span class="name">BRN</span></div>
  <div class="person">Gareth Pembly<span>CEO</span></div>
  <div class="details">482 Harlowe Street, Suite 1730<br>San Francisco, California 94111<br>Phone: 414-555-0187 | Cell: 415-555-0163<br>Fax: 415-555-0129<br>gpembly@brnqel.com | brnqel.com</div>
</section>

<section class="sheet card four">
  <div class="brand large"><span class="dot"></span><span class="name">BRN</span></div>
</section>

</body>
</html>
```